Organic Vanu (Coffee) Scrub Label for high end product

Need a product label for a coffee based body scrub called Vanu Body Scrub a 100% organic product. Our primary target is the yoga community so designs should reflect calm, perhaps incorporate eastern yoga symbology. simpler the better. Design should include both a round lid label and a rectangular wrap around label.

yoga community, people with cellulite, etc.

Community

```html
<!DOCTYPE html>
<html lang="en">
<head>
<meta charset="utf-8">
<title>Vanu Body Scrub – Label Presentation</title>
<link rel="stylesheet" href="https://fonts.googleapis.com/css2?family=Montserrat:wght@500;600&display=swap">
<style>
  :root {
    --ink: #0d0d0d;
    --paper: #ffffff;
    --panel: #efeff1;
    --pattern: #2b2b2b;
    --placeholder: #d6d6d8;
  }
  html, body {
    margin: 0;
    padding: 0;
    overflow: hidden;
  }
  body {
    width: 1200px;
    height: 848px;
    position: relative;
    background: var(--paper);
    font-family: "Montserrat", Arial, sans-serif;
    color: var(--ink);
  }
  .board-left {
    position: absolute;
    left: 0; top: 0;
    width: 600px; height: 848px;
    background: var(--paper);
  }
  .board-right {
    position: absolute;
    left: 600px; top: 0;
    width: 600px; height: 848px;
    background: var(--panel);
  }
  .mark-equation {
    position: absolute;
    left: 0; top: 104px;
    width: 600px; height: 52px;
  }
  .mark-equation .part {
    position: absolute;
    top: 4px;
    height: 44px;
    background: var(--placeholder);
    border-radius: 10px;
  }
  .mark-equation .part--lotus { left: 100px; width: 62px; }
  .mark-equation .part--bean { left: 270px; width: 22px; border-radius: 50%; }
  .mark-equation .part--combined { left: 385px; width: 100px; }
  .mark-equation .operator {
    position: absolute;
    top: 4px;
    width: 40px;
    margin-left: -20px;
    font-weight: 600;
    font-size: 40px;
    line-height: 44px;
    text-align: center;
  }
  .mark-equation .operator--plus { left: 228px; }
  .mark-equation .operator--equals { left: 345px; }
  .wrap-label--small {
    position: absolute;
    left: 150px; top: 352px;
    width: 286px; height: 261px;
  }
  .lid-label {
    position: absolute;
    left: 158px; top: 42px;
    width: 290px; height: 290px;
  }
  .wrap-label--large {
    position: absolute;
    left: 83px; top: 376px;
    width: 443px; height: 404px;
  }
  .label-text {
    font-family: "Montserrat", Arial, sans-serif;
    font-weight: 600;
  }
</style>
</head>
<body>

<svg width="0" height="0" style="position:absolute" aria-hidden="true">
  <defs>
    <symbol id="wrap-label" viewBox="0 0 443 404">
      <rect width="443" height="404" fill="#0d0d0d"/>
      <rect x="0" y="0" width="443" height="160" fill="#2b2b2b" role="img" aria-label="Repeating lotus pattern"/>
      <rect x="0" y="244" width="443" height="160" fill="#2b2b2b" role="img" aria-label="Repeating lotus pattern"/>
      <rect x="0" y="160" width="443" height="84" fill="#ffffff"/>
      <circle cx="222" cy="202" r="124" fill="#ffffff"/>
      <circle cx="222" cy="202" r="115" fill="#0d0d0d"/>
      <g fill="#ffffff">
        <circle cx="180" cy="112" r="2"/>
        <circle cx="199" cy="107" r="2.6"/>
        <circle cx="222" cy="104" r="4"/>
        <circle cx="245" cy="107" r="2.6"/>
        <circle cx="264" cy="112" r="2"/>
        <circle cx="184" cy="290" r="2"/>
        <circle cx="260" cy="290" r="2"/>
      </g>
      <text class="label-text" x="222" y="214" text-anchor="middle" font-size="60" fill="#ffffff">Vanu</text>
      <text class="label-text" x="222" y="258" text-anchor="middle" font-size="19" fill="#ffffff" letter-spacing="0.5">BODY SCRUB</text>
      <g class="label-text" font-size="11" fill="#0d0d0d" text-anchor="middle" letter-spacing="2">
        <text x="52" y="196">ORGANIC</text>
        <text x="52" y="214">COFFEE</text>
        <text x="52" y="232">SCRUB</text>
        <text x="392" y="196">100%</text>
        <text x="392" y="214">NATURAL</text>
        <text x="392" y="232">PRODUCT</text>
      </g>
    </symbol>
  </defs>
</svg>

<section class="board-left">
  <div class="mark-equation">
    <div class="part part--lotus" role="img" aria-label="Lotus symbol"></div>
    <span class="operator operator--plus">+</span>
    <div class="part part--bean" role="img" aria-label="Coffee bean"></div>
    <span class="operator operator--equals">=</span>
    <div class="part part--combined" role="img" aria-label="Lotus and coffee bean combined mark"></div>
  </div>

  <svg class="wrap-label--small" viewBox="0 0 443 404" role="img" aria-label="Vanu Body Scrub wrap-around label">
    <use href="#wrap-label" width="443" height="404"/>
  </svg>
</section>

<section class="board-right">
  <svg class="lid-label" viewBox="0 0 290 290" role="img" aria-label="Vanu Body Scrub round lid label">
    <defs>
      <path id="banner-curve" d="M44 204 Q145 262 246 204"/>
    </defs>
    <circle cx="145" cy="145" r="145" fill="#0d0d0d"/>
    <g fill="#ffffff">
      <circle cx="105" cy="38" r="2"/>
      <circle cx="124" cy="34" r="2.6"/>
      <circle cx="145" cy="31" r="4"/>
      <circle cx="166" cy="34" r="2.6"/>
      <circle cx="185" cy="38" r="2"/>
    </g>
    <text class="label-text" x="145" y="136" text-anchor="middle" font-size="60" fill="#ffffff">Vanu</text>
    <text class="label-text" x="145" y="180" text-anchor="middle" font-size="19" fill="#ffffff" letter-spacing="0.5">BODY SCRUB</text>
    <path d="M44 204 Q145 262 246 204" fill="none" stroke="#ffffff" stroke-width="20"/>
    <text class="label-text" font-size="11" fill="#0d0d0d" letter-spacing="1.5" dy="4">
      <textPath href="#banner-curve" startOffset="50%" text-anchor="middle">100% NATURAL PRODUCT</textPath>
    </text>
  </svg>

  <svg class="wrap-label--large" viewBox="0 0 443 404" role="img" aria-label="Vanu Body Scrub wrap-around label, flat">
    <use href="#wrap-label" width="443" height="404"/>
  </svg>
</section>

</body>
</html>
```